Super elegant, crisp & clean Business card design required

We recently upgraded our branding - which is on our website - tavorelstudio.com

I would like a simple, yet elegant, clean business card design please.

The font of my logo is Cinzel - and because of the natural colour - it's best to have this on a black background.

I would like to have the back of the business card - with simply my logo.

PLEASE DO NOT SUBMIT A COMPLICATED / UNCLEAN DESIGN

Industry/Entity Type

Business

Contact Information for Business Card

Dalvik Ostrander Photography

Font styles to use
Other font styles liked:
• Cinzel

Requirements
Must have
• A backpage with nothing but my logo
• Simple design - stands out
Should not have
• Colour that dont align with my logo
• Over complicated '/ non symmetrical design

```html
<!DOCTYPE html>
<html lang="en">
<head>
<meta charset="utf-8">
<title>Dalvik Ostrander Photography — Business Card</title>
<link rel="stylesheet" href="https://fonts.googleapis.com/css2?family=Cinzel:wght@400&display=swap">
<style>
  :root {
    --page: #ffffff;
    --card-front: #000000;
    --bronze: #85755c;
  }
  * { margin: 0; padding: 0; box-sizing: border-box; }
  html, body {
    width: 909px;
    height: 1200px;
    overflow: hidden;
    background: var(--page);
  }
  .sheet {
    position: relative;
    width: 909px;
    height: 1200px;
    font-family: "Cinzel", serif;
    color: var(--bronze);
  }
  .card-front {
    position: absolute;
    left: 18px;
    top: 0;
    width: 845px;
    height: 546px;
    background: var(--card-front);
  }
  .brand-name {
    position: absolute;
    left: 0;
    right: 0;
    top: 254px;
    text-align: center;
    font-size: 30px;
    font-weight: 400;
    letter-spacing: 0.5px;
    color: var(--bronze);
  }
  .card-back {
    position: absolute;
    left: 18px;
    top: 560px;
    width: 845px;
    height: 640px;
    text-align: center;
  }
  .studio-title {
    position: absolute;
    left: 0;
    right: 0;
    top: 282px;
    font-size: 32px;
    font-weight: 400;
    letter-spacing: 0.3px;
  }
  .contact-line {
    position: absolute;
    left: 0;
    right: 0;
    font-size: 14.5px;
    font-weight: 400;
    line-height: 1;
  }
  .contact-main { top: 336px; }
  .contact-web { top: 355px; }
  .sep { padding: 0 4px; }
</style>
</head>
<body>
  <main class="sheet">
    <section class="card-front" aria-label="Card front">
      <p class="brand-name">Dalvik Ostrander Photography</p>
    </section>

    <section class="card-back" aria-label="Card back">
      <h1 class="studio-title">Dalvik Ostrander Photography</h1>
      <p class="contact-line contact-main">
        07700900318<span class="sep">•</span>London, United kingdom<span class="sep">&nbsp;•</span>hello@tavorelstudio.com
      </p>
      <p class="contact-line contact-web">tavorelstudio.com</p>
    </section>
  </main>
</body>
</html>
```